Business cards & stationery for a cloth diaper retailer
Natural & Organic Baby Products
Bright & Fun-filled
Marisol Treveck
Carvale, MD 20843
info@dotsnugnest.com
www.dotsnugnest.com
My business is web-based so the website address needs to be highlighted on the card.
Services include:
- Cloth diapering workshops
- Newborn rental cloth diaper trial package
- Private In-Home Consults
- Office/Showroom hours

```html
<!DOCTYPE html>
<html lang="en">
<head>
<meta charset="utf-8">
<title>Dot's Snug Nest – Business Card</title>
<link rel="stylesheet" href="https://fonts.googleapis.com/css2?family=Nunito:wght@400;600;700;800&display=swap">
<style>
  :root {
    --bg: #2b2b2b;
    --card: #ffffff;
    --green: #7cc242;
    --orange: #e8893a;
    --tan: #d9a477;
    --tan-dark: #c98e5e;
    --text: #555555;
    --muted: #8a8a8a;
    --baby-light: #f6d7b8;
    --baby-dark: #cfe7b4;
  }
  * { box-sizing: border-box; margin: 0; padding: 0; }
  html, body { width: 1200px; height: 901px; overflow: hidden; }
  body {
    background: var(--bg);
    font-family: "Nunito", sans-serif;
    display: flex;
    flex-direction: column;
    align-items: center;
    justify-content: center;
    gap: 50px;
  }
  .card {
    position: relative;
    width: 580px;
    height: 330px;
    background: var(--card);
    border-radius: 16px;
    overflow: hidden;
    box-shadow: 0 14px 30px rgba(0,0,0,.5);
  }
  .band {
    position: absolute;
    left: 0; right: 0; bottom: 0;
    height: 44px;
    background: linear-gradient(var(--tan), var(--tan-dark));
    border-top: 4px solid var(--green);
    display: flex;
    align-items: center;
    justify-content: center;
  }
  .band .url {
    color: #fff;
    font-weight: 700;
    font-size: 18px;
    letter-spacing: 5px;
  }
  .illustration {
    position: absolute;
    border-radius: 50%;
    background: radial-gradient(circle at 45% 40%, var(--baby-light) 0 55%, var(--baby-dark) 75%);
  }
  /* back */
  .back .services {
    position: absolute;
    left: 40px; top: 48px;
  }
  .services h2 {
    color: var(--green);
    font-size: 26px;
    font-weight: 800;
    margin-bottom: 14px;
  }
  .services ul { list-style: none; }
  .services li {
    display: flex;
    align-items: center;
    gap: 10px;
    color: var(--text);
    font-size: 16px;
    font-weight: 600;
    margin-bottom: 9px;
  }
  .services li svg { flex: none; }
  .back .illustration { right: 34px; top: 34px; width: 120px; height: 120px; }
  /* front */
  .front .illustration.left { left: 26px; top: 22px; width: 110px; height: 110px; }
  .front .illustration.right { right: 26px; top: 120px; width: 112px; height: 112px; }
  .brand {
    position: absolute;
    left: 148px; top: 52px;
    display: flex;
    align-items: center;
    gap: 8px;
    color: var(--green);
    font-size: 34px;
    font-weight: 800;
  }
  .brand .dot { width: 14px; height: 14px; border-radius: 50%; background: var(--green); }
  .details { position: absolute; left: 148px; top: 118px; color: var(--text); }
  .details .name { color: var(--orange); font-size: 22px; font-weight: 800; margin-bottom: 4px; }
  .details .city { font-size: 17px; font-weight: 600; margin-bottom: 12px; }
  .details .line { display: flex; align-items: center; gap: 8px; font-size: 15px; font-weight: 600; margin-bottom: 4px; }
</style>
</head>
<body>

<section class="card back" aria-label="Card back">
  <div class="services">
    <h2>Services</h2>
    <ul>
      <li><svg width="14" height="14"><circle cx="7" cy="7" r="6" fill="#7cc242"/></svg>Newborn rental cloth diaper trial package</li>
      <li><svg width="14" height="14"><circle cx="7" cy="7" r="6" fill="#7cc242"/></svg>Cloth diapering workshops</li>
      <li><svg width="14" height="14"><circle cx="7" cy="7" r="6" fill="#7cc242"/></svg>Private In-Home Consults</li>
      <li><svg width="14" height="14"><circle cx="7" cy="7" r="6" fill="#7cc242"/></svg>Office/Showroom hours</li>
    </ul>
  </div>
  <div class="illustration" role="img" aria-label="Cartoon baby sitting with green leaves"></div>
  <div class="band"><span class="url">www.dotsnugnest.com</span></div>
</section>

<section class="card front" aria-label="Card front">
  <div class="illustration left" role="img" aria-label="Cartoon baby holding a green sprig"></div>
  <div class="brand"><span class="dot"></span>Dot's Snug Nest</div>
  <div class="details">
    <p class="name">Marisol Treveck</p>
    <p class="city">Carvale, MD 20843</p>
    <p class="line">
      <svg width="14" height="14" viewBox="0 0 24 24"><path fill="#e8893a" d="M6.6 10.8a15 15 0 0 0 6.6 6.6l2.2-2.2c.3-.3.7-.4 1-.2 1.1.4 2.3.6 3.6.6.6 0 1 .4 1 1V20c0 .6-.4 1-1 1A17 17 0 0 1 3 4c0-.6.4-1 1-1h3.5c.6 0 1 .4 1 1 0 1.3.2 2.5.6 3.6.1.3 0 .7-.2 1z"/></svg>
      555-014-2290
    </p>
    <p class="line">
      <svg width="14" height="14" viewBox="0 0 24 24"><rect x="4" y="8" width="16" height="10" rx="2" fill="#e8893a"/><rect x="7" y="3" width="10" height="6" fill="#e8893a"/></svg>
      555-014-2290
    </p>
    <p class="line">
      <svg width="14" height="14" viewBox="0 0 24 24"><rect x="2" y="5" width="20" height="14" rx="2" fill="#e8893a"/><path d="M2 6l10 7 10-7" stroke="#fff" stroke-width="2" fill="none"/></svg>
      info@dotsnugnest.com
    </p>
  </div>
  <div class="illustration right" role="img" aria-label="Cartoon baby sitting among green leaves"></div>
  <div class="band"><span class="url">www.dotsnugnest.com</span></div>
</section>

</body>
</html>
```